Kindlewellharborway.com is URL - need full website design

We need a website design created for our new business, Kindlewell Harborway Associates. Our services include mastermind groups, speaking & workshops, life coaching, leadership assessment and spiritual enrichment. Our design colors are purple, gold and white. Our final web design should reflect and communicate positive growth, learning and professional development in all endeavors. Our budget is $618.00. Need 8 pages on website.
Updates
Correction: Budget increased to $618.00 Added Monday, March 7, 2016
Target Market(s)
Churches, mid to large organizations, schools, universities, and individuals
Industry/Entity Type
Life Coaching
Logo Text
Kindlewell Harborway Associates
Coding
Coded - Design and coding required
Number of Pages Required
5+ page
Requirements
Must have
- email accounts
- A Page to place orders
- Need to add to FB, Chirper, Livecast, Clipshare, and Callwave
- Logo Design:
- Need only 1 globe. Base color : purple. Continents color: gold & lines color: white
- Would like a hand holding the globe
- Sunshine rays over top - either white or gold
- Name: "Kindlewell Harborway" in center of globe & "International" at bottom of globe sort of rounded.

```html
<!DOCTYPE html>
<html lang="en">
<head>
<meta charset="utf-8">
<title>Kindlewell Harborway Associates</title>
<link rel="stylesheet" href="https://fonts.googleapis.com/css2?family=Roboto:ital,wght@0,300;0,400;0,500;0,700;1,400&family=Open+Sans:ital,wght@0,400;0,600;1,400;1,600&display=swap">
<style>
:root{
  --orange:#f07a1a;
  --orange-dark:#e06d12;
  --purple:#5a2c8c;
  --purple-deep:#452070;
  --ink:#333333;
  --text:#555555;
  --muted:#777777;
  --card:#f4f4f4;
  --card-line:#e2e2e2;
  --white:#ffffff;
  --black:#1a1a1a;
}
*{box-sizing:border-box;margin:0;padding:0}
html,body{width:1200px;height:2560px;overflow:hidden;background:var(--white)}
body{position:relative;font-family:'Open Sans',Arial,sans-serif;color:var(--text)}
.abs{position:absolute}

/* header */
.site-header{position:absolute;left:0;top:0;width:1200px;height:96px;background:var(--white);box-shadow:0 1px 3px rgba(0,0,0,.08);z-index:2}
.brand{position:absolute;left:99px;top:26px;display:flex;align-items:center;gap:12px}
.brand-mark{width:40px;height:40px;border-radius:50%;background:var(--purple)}
.brand-name{font-family:'Roboto',sans-serif;font-weight:700;font-size:20px;color:var(--ink);letter-spacing:.5px;line-height:1}
.main-nav{position:absolute;right:0;top:0;height:96px;display:flex}
.main-nav a{display:block;height:96px;line-height:100px;padding:0 19px;font-family:'Roboto',sans-serif;font-size:13px;color:var(--ink);text-decoration:none;text-transform:uppercase}
.main-nav a.active{background:var(--orange);color:var(--white);width:79px;padding:0;text-align:center;margin-right:24px}
.main-nav .home-slot{order:0}

/* hero */
.hero{position:absolute;left:0;top:96px;width:1200px;height:534px}
.hero-photo{position:absolute;inset:0;background:radial-gradient(ellipse at 20% 10%,#dfe8f3 0%,rgba(223,232,243,0) 40%),linear-gradient(160deg,#8fa9cf 0%,#5d7fb4 40%,#3d5a95 70%,#6b6fa8 100%)}
.hero-title{position:absolute;left:716px;top:196px;font-family:'Roboto',sans-serif;font-weight:500;font-size:52px;color:var(--white);letter-spacing:.5px;line-height:1}
.hero-text{position:absolute;left:717px;top:262px;width:330px;font-size:14px;line-height:21px;color:var(--white)}
.hero-btn{position:absolute;left:717px;top:322px;width:157px;height:43px;background:var(--orange);color:var(--white);font-family:'Roboto',sans-serif;font-size:15px;font-weight:500;text-align:center;line-height:43px}
.slider-arrow{position:absolute;top:276px;width:34px;height:34px;border-radius:50%;background:rgba(60,60,60,.55)}
.slider-arrow.prev{left:24px}
.slider-arrow.next{right:24px}
.slider-arrow svg{display:block}

/* services */
.services-intro{position:absolute;left:97px;top:700px;width:312px}
.section-heading{font-family:'Roboto',sans-serif;font-size:26px;color:var(--orange);font-weight:400}
.services-intro p{margin-top:12px;font-size:11.5px;line-height:20px;color:var(--muted)}
.service-card{position:absolute;width:324px;height:187px;background:var(--card);border:1px solid var(--card-line)}
.service-icon{position:absolute;left:24px;top:26px;width:65px;height:65px;border-radius:50%;background:var(--orange)}
.service-icon svg{display:block}
.service-title{position:absolute;left:112px;top:22px;font-family:'Roboto',sans-serif;font-size:18px;color:var(--ink);font-weight:400}
.service-rule{position:absolute;left:112px;top:54px;width:60px;height:2px;background:var(--orange)}
.service-text{position:absolute;left:112px;top:70px;width:190px;font-size:11px;line-height:20px;color:var(--text)}
.service-more{position:absolute;left:112px;top:142px;font-size:13px;color:var(--muted)}

/* welcome */
.welcome{position:absolute;left:0;top:1110px;width:1200px;text-align:center}
.welcome h2{font-family:'Roboto',sans-serif;font-weight:400;font-size:36px;color:var(--ink)}
.welcome h2 span{color:var(--orange)}
.welcome p{width:920px;margin:14px auto 0;font-size:11.5px;line-height:20px;color:var(--text)}
.welcome-btn{position:absolute;left:515px;top:1250px;width:170px;height:42px;background:var(--orange);color:var(--white);font-family:'Roboto',sans-serif;font-size:16px;text-align:center;line-height:42px;border-radius:2px;z-index:1}

/* testimonials */
.testimonials{position:absolute;left:0;top:1284px;width:1200px;height:517px}
.testimonials svg.band{position:absolute;inset:0}
.testimonials-title{position:absolute;left:0;top:140px;width:1200px;text-align:center;font-family:'Roboto',sans-serif;font-size:30px;color:var(--white);font-weight:400}
.quote{position:absolute;top:218px;width:420px;height:157px;border-left:1px solid rgba(255,255,255,.6);padding-left:29px}
.quote p{font-style:italic;font-size:13px;line-height:23px;color:var(--white);padding-top:12px}
.quote .mark{font-family:'Roboto',sans-serif;font-size:22px;vertical-align:-4px;margin-right:4px}
.quote-avatar{position:absolute;left:25px;top:85px;width:80px;height:80px;border-radius:50%;background:#d9b9a4;border:3px solid var(--white)}
.quote-name{position:absolute;left:125px;top:96px;font-style:italic;font-weight:600;font-size:15px;color:var(--white)}
.quote-org{position:absolute;left:125px;top:126px;font-style:italic;font-size:13px;color:var(--white)}

/* blog */
.blog-title{position:absolute;left:0;top:1795px;width:1200px;text-align:center;font-family:'Roboto',sans-serif;font-size:30px;color:var(--ink);font-weight:400}
.blog-divider{position:absolute;left:563px;top:1845px}
.post{position:absolute;top:1891px;width:308px}
.post-photo{width:308px;height:176px;border:3px solid #e8e8e8}
.post-meta{margin-top:30px;font-style:italic;font-size:13px;color:var(--orange)}
.post-meta .sep{margin:0 10px}
.post p{margin-top:12px;font-size:11px;line-height:20px;color:var(--text);width:300px}

/* footer */
.site-footer{position:absolute;left:0;top:2238px;width:1200px;height:263px;background:var(--orange)}
.footer-heading{position:absolute;top:34px;font-family:'Open Sans',sans-serif;font-weight:600;font-size:15px;color:var(--white);text-transform:uppercase}
.contact-row{position:absolute;left:97px;display:flex;gap:14px;font-size:12.5px;line-height:20px;color:var(--white)}
.contact-row svg{flex:none;margin-top:2px}
.signup-text{position:absolute;left:422px;top:68px;width:320px;font-size:11px;line-height:19px;color:var(--white)}
.field{position:absolute;left:422px;width:324px;height:40px;background:var(--white);font-size:11px;color:var(--ink);line-height:40px;padding-left:14px}
.subscribe{position:absolute;left:644px;top:175px;width:98px;height:32px;background:var(--black);color:var(--white);font-size:11px;text-align:center;line-height:32px}
.social{position:absolute;display:flex;align-items:center;gap:10px;font-size:13px;color:var(--white)}
.social i{display:block;width:26px;height:26px;border-radius:50%;border:1.5px solid var(--white)}
.copyright{position:absolute;left:0;top:2501px;width:1200px;height:59px;background:var(--black);color:var(--white);font-size:12px;text-align:center;line-height:59px}
</style>
</head>
<body>

<header class="site-header">
  <div class="brand"><span class="brand-mark"></span><span class="brand-name">KINDLEWELL HARBORWAY</span></div>
  <nav class="main-nav">
    <a class="active" href="#">Home</a>
    <a href="#">About Us</a>
    <a href="#">Our Services</a>
    <a href="#">News</a>
    <a href="#" style="padding-right:32px">Contact Us</a>
  </nav>
</header>

<section class="hero">
  <div class="hero-photo" role="img" aria-label="Open hand beneath a blue sky with sun rays and a rainbow, surrounded by floating words such as healing, mindfulness and peace"></div>
  <div class="slider-arrow prev"><svg width="34" height="34" viewBox="0 0 34 34"><path d="M19 11l-6 6 6 6" fill="none" stroke="#fff" stroke-width="2"/></svg></div>
  <div class="slider-arrow next"><svg width="34" height="34" viewBox="0 0 34 34"><path d="M15 11l6 6-6 6" fill="none" stroke="#fff" stroke-width="2"/></svg></div>
  <h1 class="hero-title">LIFE COACHING</h1>
  <p class="hero-text">Lorem ipsum dolor sit amet, consectetur adipiscing sed do eiusmod tempor incididunt ut</p>
  <div class="hero-btn">READ MORE</div>
</section>

<div class="services-intro">
  <h2 class="section-heading">Our Services</h2>
  <p>Nemo enim ipsam voluptatem quia voluptas sit aspernatur aut odit aut fugit, sed quia consequuntur magni dolores eos qui ratione voluptatem sequi nesciunt. Neque porro squam est, qui dolorem ipsum quia dolor sit amet, cttetur, adipisci velit, sed quia non numquam eius modi</p>
</div>

<div class="service-card" style="left:437px;top:678px">
  <div class="service-icon"><svg width="65" height="65" viewBox="0 0 65 65"><rect x="23" y="21" width="18" height="22" fill="none" stroke="#fff" stroke-width="2"/><path d="M27 28h10M27 33h10M27 38h6" stroke="#fff" stroke-width="1.6"/></svg></div>
  <div class="service-title">Mastermind Groups</div><div class="service-rule"></div>
  <p class="service-text">Lorem ipsum dolor sit amet, cotur adipiscing elit, sed do eiusmod tempor incididunt ut sed</p>
  <div class="service-more">Read More ↘</div>
</div>
<div class="service-card" style="left:777px;top:678px">
  <div class="service-icon"><svg width="65" height="65" viewBox="0 0 65 65"><circle cx="32.5" cy="27" r="7" fill="#fff"/><path d="M20 45c2-8 7-10 12.5-10S43 37 45 45z" fill="#fff"/></svg></div>
  <div class="service-title">Speaking &amp; Workshops</div><div class="service-rule"></div>
  <p class="service-text">Lorem ipsum dolor sit amet, cotur adipiscing elit, sed do eiusmod tempor incididunt ut sed</p>
  <div class="service-more">Read More ↘</div>
</div>
<div class="service-card" style="left:97px;top:877px">
  <div class="service-icon"><svg width="65" height="65" viewBox="0 0 65 65"><path d="M21 44c0-14 9-22 23-22 0 14-8 22-23 22z" fill="#fff"/><path d="M23 42l14-13" stroke="#f07a1a" stroke-width="1.6"/></svg></div>
  <div class="service-title">Life Coaching</div><div class="service-rule"></div>
  <p class="service-text">Lorem ipsum dolor sit amet, cotur adipiscing elit, sed do eiusmod tempor incididunt ut sed</p>
  <div class="service-more">Read More ↘</div>
</div>
<div class="service-card" style="left:437px;top:877px">
  <div class="service-icon"><svg width="65" height="65" viewBox="0 0 65 65"><path d="M23 26h7a3 3 0 1 1 5 0h7v7a3 3 0 1 0 0 5v7H23z" fill="#fff"/></svg></div>
  <div class="service-title">Leadership Assessment</div><div class="service-rule"></div>
  <p class="service-text">Lorem ipsum dolor sit amet, cotur adipiscing elit, sed do eiusmod tempor incididunt ut sed</p>
  <div class="service-more">Read More ↘</div>
</div>
<div class="service-card" style="left:777px;top:877px">
  <div class="service-icon"><svg width="65" height="65" viewBox="0 0 65 65"><circle cx="32.5" cy="32.5" r="11" fill="none" stroke="#fff" stroke-width="5"/><circle cx="32.5" cy="32.5" r="5" fill="#fff"/></svg></div>
  <div class="service-title">Spiritual Enrichment</div><div class="service-rule"></div>
  <p class="service-text">Lorem ipsum dolor sit amet, cotur adipiscing elit, sed do eiusmod tempor incididunt ut sed</p>
  <div class="service-more">Read More ↘</div>
</div>

<section class="welcome">
  <h2>Welcome To <span>Kindlewell Harborway Associates</span></h2>
  <p>Lorem ipsum dolor sit amet, consectetur adipiscing elit, sed do eiusmod tempor incididunt ut labore et dolore magna aliqua. Ut enim ad minim veniam, quis nostrud exercitation ullamco laboris nisi ut aliquip ex ea commodo consequat. Duis aute irure dolor in reprehenderit in voluptate velit esse cillum dolore eu fugiat nulla pariatur. Excepteur sint occaecat cupidatat non proident, sunt in culpa qui officia deserunt mollit anim id est laborum.</p>
</section>
<div class="welcome-btn">Read More Info</div>

<section class="testimonials">
  <svg class="band" width="1200" height="517" viewBox="0 0 1200 517" role="img" aria-label="Purple band over a photo of a woman running outdoors">
    <defs><linearGradient id="bandFill" x1="0" y1="0" x2="1" y2="1"><stop offset="0" stop-color="#4a2478"/><stop offset=".55" stop-color="#5a2c8c"/><stop offset="1" stop-color="#6a3a96"/></linearGradient></defs>
    <polygon points="0,0 600,70 1200,0 1200,517 600,449 0,517" fill="url(#bandFill)"/>
  </svg>
  <h2 class="testimonials-title">WHAT THEY SAY</h2>
  <div class="quote" style="left:133px">
    <p><span class="mark">“</span>Lorem ipsum dolor sit amet, consectetur adipiscing elit, sed do eiusmod tempor incididunt ut labore et dolore magna aliqua. Ut enim ad minim veniam, quis nostrud exercitation..</p>
    <div class="quote-avatar" role="img" aria-label="Client portrait"></div>
    <div class="quote-name">John Doe</div>
    <div class="quote-org">Kindlewell Harborway Associates,</div>
  </div>
  <div class="quote" style="left:655px">
    <p><span class="mark">“</span>Lorem ipsum dolor sit amet, consectetur adipiscing elit, sed do eiusmod tempor incididunt ut labore et dolore magna aliqua. Ut enim ad minim veniam, quis nostrud exercitation..</p>
    <div class="quote-avatar" role="img" aria-label="Client portrait" style="background:#c98d6e"></div>
    <div class="quote-name">John Doe</div>
    <div class="quote-org">Kindlewell Harborway Associates,</div>
  </div>
</section>

<h2 class="blog-title">LATEST BLOG</h2>
<svg class="blog-divider" width="74" height="14" viewBox="0 0 74 14"><line x1="8" y1="7" x2="66" y2="7" stroke="#4a6fa5" stroke-width="1.5"/><circle cx="6" cy="7" r="4.5" fill="#fff" stroke="#4a6fa5" stroke-width="1.5"/><circle cx="37" cy="7" r="4.5" fill="#fff" stroke="#4a6fa5" stroke-width="1.5"/><circle cx="68" cy="7" r="4.5" fill="#fff" stroke="#4a6fa5" stroke-width="1.5"/></svg>

<article class="post" style="left:99px">
  <div class="post-photo" role="img" aria-label="Person meditating at sunset by the sea" style="background:linear-gradient(180deg,#e89a2a 0%,#c8561a 60%,#5a2a10 100%)"></div>
  <div class="post-meta">JAN 21, 2016 <span class="sep">\</span> 2 COMMENTS</div>
  <p>Lorem ipsum dolor sit amet, consectetur adipiscing elit. Sed blandit massa vel mauris sollicitudin dignissim. Lorem ipsum dolor sit amet, consectetur</p>
</article>
<article class="post" style="left:444px">
  <div class="post-photo" role="img" aria-label="Woman raising her arms toward the sun on a beach" style="background:linear-gradient(180deg,#f5c330 0%,#eea020 55%,#8a5a14 100%)"></div>
  <div class="post-meta">JAN 21, 2016 <span class="sep">\</span> 2 COMMENTS</div>
  <p>Lorem ipsum dolor sit amet, consectetur adipiscing elit. Sed blandit massa vel mauris sollicitudin dignissim. Lorem ipsum dolor sit amet, consectetur</p>
</article>
<article class="post" style="left:792px">
  <div class="post-photo" role="img" aria-label="Smiling couple riding bicycles in a city street" style="background:linear-gradient(135deg,#b7a79a 0%,#c27e6a 50%,#7a5a5a 100%)"></div>
  <div class="post-meta">JAN 21, 2016 <span class="sep">\</span> 2 COMMENTS</div>
  <p>Lorem ipsum dolor sit amet, consectetur adipiscing elit. Sed blandit massa vel mauris sollicitudin dignissim. Lorem ipsum dolor sit amet, consectetur</p>
</article>

<footer class="site-footer">
  <div class="footer-heading" style="left:99px">Contact Us</div>
  <div class="contact-row" style="top:80px"><svg width="16" height="20" viewBox="0 0 16 20"><path d="M8 19s6-7 6-11A6 6 0 0 0 2 8c0 4 6 11 6 11z" fill="none" stroke="#fff" stroke-width="1.5"/><circle cx="8" cy="8" r="2.2" fill="none" stroke="#fff" stroke-width="1.4"/></svg><div style="padding-left:4px">Kindlewell Harborway Associates<br>412 Lantern Row, Suite 210</div></div>
  <div class="contact-row" style="top:136px"><svg width="18" height="18" viewBox="0 0 18 18"><path d="M4 2l3 3-2 2c1 2 3 4 5 5l2-2 3 3-2 3C7 15 3 11 1 4z" fill="none" stroke="#fff" stroke-width="1.4"/></svg><div style="padding-left:2px">+607-555-0142</div></div>
  <div class="contact-row" style="top:170px"><svg width="18" height="14" viewBox="0 0 18 14"><rect x="1" y="1" width="16" height="12" fill="none" stroke="#fff" stroke-width="1.4"/><path d="M1 1l8 7 8-7" fill="none" stroke="#fff" stroke-width="1.4"/></svg><div style="padding-left:2px">info@kindlewellharborway.com</div></div>

  <div class="footer-heading" style="left:422px">Sign Up to Receive Email</div>
  <p class="signup-text">Excepteur sint occaecat cupidatat non proident, sunt in culpa qui Nemo enim ipsam voluptatem</p>
  <div class="field" style="top:119px">Enter Name</div>
  <div class="field" style="top:171px">Enter Email</div>
  <div class="subscribe">SUBSCRIBE</div>

  <div class="footer-heading" style="left:848px">Social Networks</div>
  <div class="social" style="left:848px;top:79px"><i></i>Facepage</div>
  <div class="social" style="left:848px;top:119px"><i></i>Chirper</div>
  <div class="social" style="left:848px;top:159px"><i></i>Livecast</div>
  <div class="social" style="left:995px;top:79px"><i></i>Clipshare</div>
  <div class="social" style="left:995px;top:119px"><i></i>Callwave</div>
</footer>

<div class="copyright">Copyright © Kindlewell Harborway Associates 2016. All rights reserved.</div>

</body>
</html>
```